Quarry - Web Design Project

We are seeking to have our website redesigned. Our current webpage is rather dated looking www.quarry-results.com We will be utilizing similar content to explain our services as what is in the website now. We do not see it at a retail portal but rather a website for those inquiring about our services as a reference check so to speak.

We wish to have a look that is considered clean, fresh, contemporary and contains a business savvy vibe.

We prefer isolated white background and also wish to retain the integrity of our Logo and colour scheme.

We are looking for something that doesnt look like it was designed at home on sitemarlo. We are hoping to find something that looks like it would reside on a tablet.

Hello designers!

We apologize for our tardiness as we have been quite preoccupied. We will be extending our invites to the end of January!

Hello All,

Please review our offer once again for updated requirements.  We are hoping to accept a design by months end.

Quarry

Target Market(s)

Business to business clients and Large manufacturers

Industry/Entity Type

Retail

Requirements
Must have
• Existing Logo

There must be an area dedicated to an intro video that will be incorporated on our landing page.

We require design of the other pages as well not only the landing page.

```html
<!DOCTYPE html>
<html lang="en">
<head>
<meta charset="utf-8">
<title>Quarry Performance Group</title>
<link href="https://fonts.googleapis.com/css2?family=Arimo:wght@400;700&family=Roboto+Condensed:wght@400;700&display=swap" rel="stylesheet">
<style>
:root{
  --red:#e00d0d;
  --red-dark:#b80a0a;
  --ink:#333;
  --grey:#555;
  --muted:#7d7d7d;
  --page:#f1f1f3;
  --panel:#fff;
  --line:#d4d4d8;
}
*{box-sizing:border-box;margin:0;padding:0}
html,body{width:1193px;height:1200px;overflow:hidden}
body{background:var(--page);font-family:"Arimo",Arial,sans-serif;color:var(--ink);position:relative}
.abs{position:absolute}

.brand{left:110px;top:28px;display:flex;align-items:center;gap:10px}
.brand-dot{width:18px;height:18px;border-radius:50%;background:var(--red)}
.brand-name{font-size:44px;color:var(--grey);font-weight:400;letter-spacing:-1px}

.social{left:814px;top:18px;display:flex;gap:7px}
.social span{width:22px;height:22px;border-radius:50%;background:#5a5a5a;display:block}
.sign-in{left:910px;top:17px;width:60px;height:24px;background:var(--red);color:#fff;font-size:15px;text-align:center;line-height:24px;border-radius:2px}
.flag{top:17px;width:40px;height:24px}
.flag-fr{left:985px}
.flag-uk{left:1042px}
.contact{right:111px;top:54px;font-size:14px;color:var(--ink);text-align:right;line-height:22px}
.contact div{display:flex;align-items:center;justify-content:flex-end;gap:8px}

.nav{left:110px;top:106px;width:972px;height:51px;background:linear-gradient(#f9f9f9,#e9e9ec);border:1px solid #d0d0d4;border-radius:3px;box-shadow:0 3px 3px rgba(0,0,0,.12);display:flex;font-family:"Roboto Condensed",Arial,sans-serif;font-size:16px;color:#444}
.nav a{color:inherit;text-decoration:none;height:100%;display:flex;align-items:center;padding:0 18px;border-right:1px solid #d0d0d4}
.nav a span{border-bottom:2px solid #bbb;padding-bottom:2px}
.nav .is-active{background:#fbfbfb;width:79px;justify-content:center;padding:0}
.nav .is-active span{border-color:var(--red)}
.search{left:862px;top:117px;width:208px;height:25px;border:1px solid #ccc;border-radius:3px;background:#f4f4f5;font-size:13px;color:#aaa;display:flex;align-items:center;gap:8px;padding-left:8px}

.arrow{top:304px;width:38px;height:38px;border-radius:50%;background:#fff;border:3px solid #bdbdbd;box-shadow:0 0 0 1px #999}
.arrow-prev{left:113px}.arrow-next{left:1043px}
.hero-title{left:179px;top:256px;font-size:40px;font-weight:700;color:var(--red);line-height:39px;letter-spacing:.3px}
.hero-sub{left:179px;top:338px;font-size:22px;color:#444;line-height:24px}
.hero-art{left:590px;top:175px;width:430px;height:295px;border-radius:40%;background:radial-gradient(ellipse at 50% 55%,rgba(230,190,30,.35),rgba(40,160,60,.25) 35%,rgba(30,80,200,.12) 60%,rgba(241,241,243,0) 75%)}
.dots{left:563px;top:480px;display:flex;gap:6px}
.dots span{width:14px;height:14px;border-radius:50%;background:#d6d6d8;box-shadow:inset 0 1px 2px rgba(0,0,0,.25)}
.dots .on{background:#8e8e90}

.welcome{left:111px;top:519px;width:971px;height:283px;background:var(--panel)}
.welcome h1{position:absolute;left:24px;top:27px;font-size:24px;font-weight:400;color:#555}
.welcome h1 em{font-style:normal;color:var(--red)}
.welcome p{position:absolute;left:24px;width:535px;font-size:16px;line-height:21px;color:var(--muted)}
.video{position:absolute;left:593px;top:31px;width:361px;height:223px;background:#000}
.video-play{position:absolute;left:158px;top:80px;width:46px;height:46px;border-radius:50%;border:3px solid #333}
.video-bar{position:absolute;left:0;bottom:0;width:100%;height:24px;background:linear-gradient(#333,#111);display:flex;align-items:center;font-size:10px;color:#ddd}

.services{left:111px;top:830px;width:971px;height:225px;border-top:3px solid #d8d8dc;border-bottom:3px solid #d8d8dc;display:flex}
.service{height:100%;text-align:center;border-right:1px solid var(--line);position:relative}
.service:last-child{border-right:none}
.service h2{font-family:"Roboto Condensed",Arial,sans-serif;font-weight:400;font-size:20px;color:#222;margin-top:22px}
.service p{font-size:14px;line-height:16px;color:#222;margin:12px auto 0;padding:0 2px}
.btn{position:absolute;top:160px;left:50%;transform:translateX(-50%);width:102px;height:32px;background:var(--red);color:#fff;font-family:"Roboto Condensed",Arial,sans-serif;font-size:17px;line-height:32px;border-bottom:2px solid var(--red-dark);border-radius:2px}

.pager{left:554px;top:1070px;display:flex;gap:12px}
.pager span{width:21px;height:21px;border-radius:50%;background:var(--red-dark);color:#fff;font-size:13px;text-align:center;line-height:21px}
.pager .cur{background:#fff;color:#333;border:1px solid #bbb}

.footer-line{left:111px;top:1116px;width:971px;height:1px;background:#d4d4d8}
.footer-nav{left:0;top:1140px;width:1193px;text-align:center;font-size:13px;color:#444}
.footer-nav .is-active{color:var(--red)}
.copy{left:0;top:1168px;width:1193px;text-align:center;font-size:13px;color:#444}
</style>
</head>
<body>

<div class="abs brand"><span class="brand-dot"></span><span class="brand-name">quarry</span></div>

<div class="abs social" aria-label="Social links"><span></span><span></span><span></span></div>
<div class="abs sign-in">Sign In</div>
<svg class="abs flag flag-fr" viewBox="0 0 40 24" aria-label="Français"><rect width="14" height="24" fill="#0a3bd9"/><rect x="14" width="12" height="24" fill="#fff"/><rect x="26" width="14" height="24" fill="#f01010"/></svg>
<svg class="abs flag flag-uk" viewBox="0 0 40 24" aria-label="English"><rect width="40" height="24" fill="#1c2f8a"/><path d="M0 0L40 24M40 0L0 24" stroke="#fff" stroke-width="5"/><path d="M0 0L40 24M40 0L0 24" stroke="#d60a0a" stroke-width="2"/><path d="M20 0V24M0 12H40" stroke="#fff" stroke-width="8"/><path d="M20 0V24M0 12H40" stroke="#d60a0a" stroke-width="4"/></svg>

<div class="abs contact">
  <div><svg width="14" height="14" viewBox="0 0 14 14"><rect width="14" height="14" rx="2" fill="#333"/><path d="M4 3c0 4 3 8 7 8l-1-2-2 0-3-3 0-2z" fill="#fff"/></svg>+1.888.555.0143</div>
  <div><svg width="18" height="12" viewBox="0 0 18 12"><rect x="1" y="1" width="16" height="10" fill="none" stroke="#333" stroke-width="1.5"/><path d="M1 1l8 6 8-6" fill="none" stroke="#333" stroke-width="1.5"/></svg>info@quarry-results.com</div>
</div>

<nav class="abs nav">
  <a class="is-active"><span>Home</span></a>
  <a><span>Who We Are</span></a>
  <a><span>Cross The Quarry</span></a>
  <a><span>Performance Solutions</span></a>
  <a><span>Sustain Solutions</span></a>
  <a style="border-right:none"><span>Join Us</span></a>
</nav>
<div class="abs search"><svg width="12" height="12" viewBox="0 0 12 12"><circle cx="5" cy="5" r="3.8" fill="none" stroke="#999" stroke-width="1.6"/><path d="M8 8l3 3" stroke="#999" stroke-width="1.8"/></svg>Search...</div>

<svg class="abs arrow arrow-prev" viewBox="0 0 32 32"><path d="M18 10l-6 6 6 6z" fill="#333"/></svg>
<svg class="abs arrow arrow-next" viewBox="0 0 32 32"><path d="M14 10l6 6-6 6z" fill="#333"/></svg>
<div class="abs hero-title">Quarry Performance<br>Group Inc.</div>
<div class="abs hero-sub">is the leading provider of profit generating<br>and people development solutions.</div>
<div class="abs hero-art" role="img" aria-label="Illustration of four coloured gears in blue, green, yellow and red, each with a running figure on top"></div>
<div class="abs dots"><span></span><span></span><span class="on"></span><span></span></div>

<section class="abs welcome">
  <h1>Welcome to <em>Quarry Performance Group</em></h1>
  <p style="top:72px">Quarry Performance Group Inc. is the leading provider of profit generating and people development solutions. With the hands-on experience of best practices, the state-of-the-art technology and in-depth information we help companies increase their efficiencies and profits. Frank, honest, committed, valuable and rewarding are words that customers use to describe the quality services provided by Quarry Performance Group.</p>
  <p style="top:209px">Learn more about us, or find the right solutions for your specific business.We will be delighted to help you achieve better business results.</p>
  <div class="video">
    <div class="video-play"><svg width="40" height="40" viewBox="0 0 40 40"><path d="M15 10l13 10-13 10z" fill="#3a3a3a"/></svg></div>
    <div class="video-bar">
      <svg width="30" height="24" viewBox="0 0 30 24"><path d="M10 6l12 6-12 6z" fill="#aaa"/></svg>
      <svg width="28" height="24" viewBox="0 0 28 24"><path d="M5 9h4l5-4v14l-5-4H5z" fill="#888"/></svg>
      <span style="margin-left:6px">0:00 / 0:00</span>
      <span style="margin-left:12px;width:180px;height:6px;background:#333;border-radius:3px;position:relative"><span style="position:absolute;left:-2px;top:-3px;width:12px;height:12px;border-radius:50%;background:#ccc"></span></span>
      <svg style="margin-left:auto;margin-right:6px" width="22" height="14" viewBox="0 0 22 14"><rect width="22" height="14" rx="2" fill="#555"/><path d="M5 10l6-6 6 6z" fill="#ddd"/></svg>
    </div>
  </div>
</section>

<section class="abs services">
  <div class="service" style="width:216px"><h2>Business Diagnostics</h2><p>Before we embark on any performance improvement initiative or development project</p><div class="btn">Learn More</div></div>
  <div class="service" style="width:268px"><h2>Executive Coaching</h2><p style="width:230px">There are many examples of executives and senior managers that have been working relentlessly yet not quite reaching their goals.</p><div class="btn">Learn More</div></div>
  <div class="service" style="width:250px"><h2>Management Development</h2><p style="width:220px">There is more than one management style. When it comes to creating an effective sales or customer driven organization</p><div class="btn">Learn More</div></div>
  <div class="service" style="width:237px"><h2>Creating Sales Culture</h2><p>In the current market, every successful organization is trying to a create and instill true sales culture across every department of their business.</p><div class="btn">Learn More</div></div>
</section>

<div class="abs pager"><span>1</span><span class="cur">2</span><span>3</span></div>

<div class="abs footer-line"></div>
<div class="abs footer-nav"><span class="is-active">Home</span> &nbsp;I&nbsp; Who We Are &nbsp;I&nbsp; Cross The Quarry &nbsp;I&nbsp; Performance Solutions &nbsp;I&nbsp; Sustain Solutions &nbsp;I&nbsp; Join Us</div>
<div class="abs copy">© 2013 Quarry Performance Group.&nbsp; All rights reserved.</div>

</body>
</html>
```